Website for a web design agency

We are a website and marketing agency. We do website design, development, and well as Brindle and Quorvia advertising and analytics. We ourselves need a new website for our own brand. We are working on some designs in-house with our own designers, but we also wanted to see what outside designers would come up with.
We are starting off with the homepage, and here is the breakdown of the sections:
https://files.brindlework.example/sheet/d/7kqTr2VnPLwXeHsaMcY4oBfJzuGNtKdWiEh3Rx9pLmQb/view?mode=share
This doc also has many links to sites we have done, which you can take screenshots of for the portfolio section.
In terms of the "look" I am going for, I want to look high-end and very beautiful designs. I found this website that I like a lot that you can use some of the elements of, just as a starting point:
http://velmarkstudio.example/layouts/pixelbarn/html/ostrevo/index.html and here is another design option they have http://velmarkstudio.example/layouts/pixelbarn/html/ostrevo/index-4.html
I'm also uploading my logo. The logo matches the gold and black look from these websites, but I would be open to switching to another color scheme if needed.
This is the link to my very old website, which you can use for some of the dummy text, and a pic of myself. I will be taking more pics of myself:
https://theplumtreeandwillowgroup.example/
We need a homepage and a portfolio page right now, but if you are the winner, we will be hiring you to make additional pages.
Updates
More designs continue to come in even today, and I want to make sure no other designers are still submitting designs.
Target Market(s)
medium and large businesses owners, and non-profits
Number of Pages Required
1 page

```html
<!DOCTYPE html>
<html lang="en">
<head>
<meta charset="utf-8">
<title>Corvane Strategies — Web Design Agency</title>
<link href="https://fonts.googleapis.com/css2?family=Poppins:ital,wght@0,400;0,500;0,600;0,700;1,400&family=Open+Sans:ital,wght@0,400;0,600;1,400&display=swap" rel="stylesheet">
<style>
:root{
  --gold:#f3b21f;
  --gold-soft:#e9a91c;
  --ink:#1f1e1c;
  --panel:#2c2a27;
  --panel-dark:#1a1917;
  --nav:#2b2926;
  --text:#ffffff;
  --muted:#d9d6d0;
  --head:'Poppins',sans-serif;
  --body:'Open Sans',sans-serif;
}
*{box-sizing:border-box;margin:0;padding:0}
html,body{width:1200px;height:4258px;overflow:hidden}
body{background:var(--ink);color:var(--text);font-family:var(--body);position:relative}
.abs{position:absolute}
section,header,footer{position:absolute;left:0;width:1200px}
.eyebrow{font-family:var(--head);font-weight:500;font-size:14px;text-decoration:underline;text-underline-offset:3px;letter-spacing:.2px;text-transform:uppercase}
.title{font-family:var(--head);font-weight:700;font-size:21px;text-transform:uppercase;letter-spacing:.2px}
.copy{font-family:var(--body);font-size:11.6px;line-height:20px;color:var(--muted);text-align:justify}
.btn{position:absolute;display:flex;align-items:center;justify-content:center;gap:5px;background:var(--panel-dark);color:var(--gold);font-family:var(--head);font-size:11.5px;font-weight:500;letter-spacing:.6px;text-transform:uppercase}
.gold-circle{border-radius:50%;background:var(--gold);display:flex;align-items:center;justify-content:center}

/* nav */
.site-nav{top:0;height:86px;background:var(--nav)}
.burger{left:79px;top:35px;width:14px}
.burger span{display:block;height:2px;background:#fff;margin-bottom:3px}
.brand{left:107px;top:28px;color:var(--gold);font-family:var(--head);font-weight:700;line-height:1}
.brand .name{font-size:19px;letter-spacing:.5px}
.brand .sub{font-size:7.5px;letter-spacing:3.4px;margin-top:2px}
.menu{font-family:var(--head);font-weight:600;font-size:10.5px}
.menu span{position:absolute;white-space:nowrap}

/* hero */
.hero{top:86px;height:588px}
.hero-photo{position:absolute;inset:0;background:linear-gradient(110deg,#b8b5b0 0%,#8f8c87 35%,#6e6c69 60%,#4b4a48 80%,#7a7874 100%)}
.hero-shade{position:absolute;inset:0;background:rgba(30,28,26,.35)}
.hero .welcome{left:339px;top:186px;font-family:var(--head);font-size:18px;text-decoration:underline;text-underline-offset:3px}
.hero h1{position:absolute;left:339px;top:208px;font-family:var(--head);font-weight:700;font-size:31px;line-height:41px;width:560px}
.hero-btn{position:absolute;left:339px;top:306px;width:160px;height:39px;border:2px solid var(--gold);border-radius:20px;font-family:var(--head);font-size:11px;display:flex;align-items:center;padding-left:25px}
.hero-btn .arrow{position:absolute;right:3px;top:3px;width:29px;height:29px}
.dots{left:80px;top:518px;display:flex;gap:17px}
.dots i{width:13px;height:13px;border-radius:50%;background:#2b2926;border:2px solid #555;display:block}
.dots i.on{background:var(--gold);border-color:var(--gold)}

/* clients */
.clients{top:674px;height:156px;background:var(--panel)}
.client{position:absolute;top:60px;transform:translateX(-50%);text-align:center;font-family:var(--head);color:#c9c6c1}
.client b{display:block;font-size:18px;font-weight:500;letter-spacing:2px}
.client small{display:block;font-size:7px;letter-spacing:2px;margin-top:3px}
.clients .chev{position:absolute;top:62px;color:var(--gold);font-size:18px}
.cdots{left:562px;top:134px;display:flex;gap:8px}
.cdots i{width:4px;height:4px;border-radius:50%;background:#666;display:block}
.cdots i.on{background:var(--gold)}

/* about */
.about{top:830px;height:522px;background:var(--ink)}
.about-card{left:757px;top:41px;width:309px;height:440px;background:var(--panel);border:6px solid var(--panel-dark);border-radius:36px 10px 36px 10px}
.about-card .photo{position:absolute;left:9px;top:9px;width:281px;height:205px;background:linear-gradient(135deg,#f0ede6,#cfd8c9 55%,#e8b28a)}
.about-card .quote{position:absolute;left:22px;top:221px;width:256px;font-style:italic;font-size:10.5px;line-height:17.5px;text-align:center;color:var(--muted)}
.avatar{border-radius:50%;background:linear-gradient(#d8d4cd,#8a857e);border:2px solid #fff}

/* services */
.services{top:1352px;height:610px;background:var(--panel)}
.svc-card{left:132px;top:41px;width:311px;height:529px;border:6px solid var(--panel-dark);border-radius:34px 10px 34px 10px;background:var(--panel)}
.svc-card .shot{position:absolute;left:12px;top:262px;width:275px;height:177px;border-radius:0 0 30px 0;background:linear-gradient(135deg,#6fa8c7,#9ccde0 50%,#e6d6b2)}
.tile{position:absolute;width:180px;height:218px;background:var(--ink);text-align:center}
.tile .gold-circle{width:78px;height:78px;margin:17px auto 0}
.tile h3{font-family:var(--head);font-weight:600;font-size:15.5px;line-height:17px;margin-top:17px}
.tile p{font-size:10.5px;line-height:17px;color:var(--muted);margin:12px auto 0;width:130px}

/* why */
.why{top:1962px;height:575px;background:var(--ink)}
.side{position:absolute;top:41px;width:155px;height:498px;background:var(--panel)}
.ring{position:absolute;left:24px;width:106px;height:106px}
.ring span{position:absolute;inset:0;display:flex;align-items:center;justify-content:center;font-family:var(--head);font-size:21px;font-weight:500}
.rate{position:absolute;left:17px;width:120px;text-align:center;font-family:var(--head);font-size:14px;border-top:1.5px solid #fff;padding-top:3px}
.perk{position:absolute;width:199px;height:127px;text-align:center}
.perk.fill{background:var(--panel)}
.perk .gold-circle{width:78px;height:78px;margin:8px auto 0}
.perk h4{font-family:var(--head);font-weight:500;font-size:13.5px;margin-top:12px}

/* portfolio */
.portfolio{top:2537px;height:571px;background:var(--panel)}
.tab{position:absolute;font-family:var(--head);font-weight:500;font-size:11px;line-height:12px}
.tab-active{left:327px;top:53px;width:162px;height:58px;border:1.5px solid var(--gold);border-bottom:none;background:var(--panel)}
.panel{left:327px;top:108px;width:729px;height:418px;border:1.5px solid var(--gold);border-top:none}
.panel-top{left:489px;top:108px;width:567px;height:1.5px;background:var(--gold)}
.thumb{position:absolute;top:202px;width:44px;height:121px;background:linear-gradient(#c0392b 0 10%,#e9e5de 10% 55%,#7b8fa6 55% 70%,#f1efea 70%)}
.thumb-label{position:absolute;top:345px;width:100px;transform:translateX(-50%);text-align:center;font-family:var(--head);font-size:14px;line-height:15px;text-decoration:underline}

/* testimony */
.testimony{top:3108px;height:388px;background:var(--ink)}
.t-card{left:132px;top:41px;width:620px;height:306px;border:5px solid var(--panel);border-radius:10px 36px 10px 36px}
.t-quote{position:absolute;left:52px;top:26px;width:526px;font-style:italic;font-size:11.5px;line-height:17.4px;text-align:center;color:var(--muted)}
.t-photo{left:764px;top:140px;width:296px;height:200px;border-radius:0 0 36px 0;background:linear-gradient(120deg,#4a4541,#9a9188 45%,#d9d4cc)}

/* contact */
.contact{top:3496px;height:389px;background:var(--panel)}
.call-card{left:139px;top:116px;width:297px;height:264px;background:var(--panel-dark);border-radius:60px 0 40px 0;overflow:hidden}
.call-card .photo{position:absolute;left:0;top:0;width:297px;height:140px;background:linear-gradient(180deg,#ffffff 0 35%,#e6c9a4 60%,#a98466);border-radius:60px 0 0 0}
.form{left:446px;top:41px;width:620px;height:306px;border:5px solid var(--panel-dark);border-radius:10px 36px 10px 36px}
.field-label{position:absolute;font-family:var(--head);font-size:12px}
.field{position:absolute;height:33px;background:#fff;font-size:10px;color:#999;padding:10px 8px}

/* footer */
.site-footer{top:3885px;height:373px;background:var(--ink)}
.f-head{position:absolute;top:66px;font-family:var(--head);font-size:13px;text-decoration:underline;text-underline-offset:3px}
.f-list{position:absolute;top:98px;font-family:var(--head);font-size:12px;line-height:26.5px}
.bottom{position:absolute;left:0;top:347px;width:1200px;height:26px;background:var(--panel);font-size:9px;color:#aaa;padding:8px 139px}
</style>
</head>
<body>

<header class="site-nav">
  <div class="abs burger"><span></span><span></span><span></span></div>
  <div class="abs brand"><div class="name">CORVANE</div><div class="sub">STRATEGIES</div></div>
  <nav class="abs menu" style="left:0;top:37px">
    <span style="left:420px">HOME</span>
    <span style="left:505px">ABOUT</span>
    <span style="left:594px">SERVICES</span>
    <span style="left:694px">WHY CHOSE US?</span>
    <span style="left:829px">PORTFOLIO</span>
    <span style="left:939px">TESTIMONY</span>
    <span style="left:1051px">CONTACT US</span>
  </nav>
</header>

<section class="hero">
  <div class="hero-photo" role="img" aria-label="Photo of a bright office with a developer working at a monitor beside a whiteboard"></div>
  <div class="hero-shade"></div>
  <div class="abs welcome">Welcome To Corvane</div>
  <h1>Let’s Build Your Business Online, Together.</h1>
  <div class="hero-btn">CONTACT US
    <div class="gold-circle arrow"><svg width="12" height="12" viewBox="0 0 12 12"><path d="M1 6h9M6 2l4 4-4 4" stroke="#fff" stroke-width="1.6" fill="none"/></svg></div>
  </div>
  <div class="abs dots"><i></i><i></i><i></i><i class="on"></i><i></i><i></i></div>
</section>

<section class="clients">
  <span class="chev" style="left:148px">‹</span>
  <span class="chev" style="left:1042px">›</span>
  <div class="client" style="left:231px"><b>MARLOW</b><small>STUDIO</small></div>
  <div class="client" style="left:415px"><b>QUILLON</b></div>
  <div class="client" style="left:600px"><b>TESSARO</b></div>
  <div class="client" style="left:785px"><b>NORTHBAY</b></div>
  <div class="client" style="left:970px"><b>RAVELIN</b><small>property group</small></div>
  <div class="abs cdots"><i></i><i></i><i></i><i></i><i class="on"></i><i></i></div>
</section>

<section class="about">
  <div class="abs eyebrow" style="left:139px;top:47px">About Us</div>
  <h2 class="abs title" style="left:139px;top:77px">Welcome To Corvane</h2>
  <p class="abs copy" style="left:154px;top:116px;width:515px">Lorem ipsum dolor sit amet, consectetur adipiscing elit, sed do eiusmod tempor incididunt ut labore et dolore magna aliqua. Vulputate dignissim suspendisse in est ante. Faucibus turpis in eu mi bibendum neque. Sodales ut etiam sit amet nisl purus. Velit laoreet id donec ultrices tincidunt.</p>
  <p class="abs copy" style="left:154px;top:218px;width:515px">Lorem ipsum dolor sit amet, consectetur adipiscing elit, sed do eiusmod tempor incididunt ut labore et dolore magna aliqua. Tempor orci eu lobortis elementum nibh tellus molestie. Sagittis orci a scelerisque purus semper eget duis at. Commodo odio aenean sed adipiscing diam donec. Faucibus scelerisque eleifend donec pretium vulputate sapien. Cursus vitae congue mauris rhoncus aenean vel elit scelerisque mauris. Ultrices gravida dictum fusce ut placerat. Volutpat commodo sed egestas egestas fringilla phasellus faucibus.</p>
  <div class="btn" style="left:139px;top:396px;width:149px;height:37px">Know More <span>»</span></div>
  <div class="abs about-card">
    <div class="photo" role="img" aria-label="Photo of a team reviewing printed charts on a desk"></div>
    <p class="quote">Nisl nunc mi ipsum faucibus vitae aliquet. Non sodales neque sodales ut etiam sit amet nisl purus. Adipiscing at in tellus integer feugiat scelerisque. Dignissim enim sit amet venenatis urna cursus eget. Volutpat est velit egestas dui id. Viverra justo nec ultrices dui sapien eget mi proin. Eget sit amet tellus cras.</p>
    <div class="abs avatar" role="img" aria-label="Portrait of the founder" style="left:77px;top:374px;width:44px;height:44px"></div>
    <div class="abs" style="left:129px;top:380px;font-family:var(--head);font-size:12px;line-height:14px">Dorian Vale<br><span style="font-size:9.5px">WEB DEVELOPER</span></div>
  </div>
</section>

<section class="services">
  <div class="abs svc-card">
    <div class="abs eyebrow" style="left:12px;top:21px">Services</div>
    <h2 class="abs title" style="left:12px;top:51px;font-size:20px">How Can We Help You?</h2>
    <p class="abs copy" style="left:12px;top:85px;width:275px">Lorem ipsum dolor sit amet, consectetur adipiscing elit, sed do eiusmod tempor incididunt ut labore et dolore magna aliqua. Vulputate dignissim suspendisse in est ante. Faucibus turpis in eu mi bibendum neque. Sodales ut etiam sit amet nisl purus. Velit laoreet id donec ultrices tincidunt.</p>
    <div class="shot" role="img" aria-label="Illustration of a hand using a tablet showing website layouts"></div>
    <div class="btn" style="left:12px;top:461px;width:149px;height:35px">Know More <span>»</span></div>
  </div>

  <div class="tile" style="left:471px;top:69px"><div class="gold-circle"><svg width="40" height="40" viewBox="0 0 40 40" fill="none" stroke="#fff" stroke-width="2"><rect x="7" y="8" width="26" height="18" rx="1"/><path d="M20 26v6M13 34h14"/><circle cx="20" cy="17" r="4"/></svg></div><h3>Websites</h3><p>Lorem ipsum dolor sit amet consectetur adipiscing elit dolor</p></div>
  <div class="tile" style="left:666px;top:69px"><div class="gold-circle"><svg width="40" height="40" viewBox="0 0 40 40" fill="none" stroke="#fff" stroke-width="2"><rect x="6" y="8" width="28" height="19" rx="1"/><path d="M20 27v5M13 33h14M15 20l8-7M19 21l5-4"/></svg></div><h3>Landing Pages</h3><p>Lorem ipsum dolor sit amet consectetur adipiscing elit dolor</p></div>
  <div class="tile" style="left:861px;top:69px"><div class="gold-circle"><svg width="40" height="40" viewBox="0 0 40 40" fill="none" stroke="#fff" stroke-width="2"><circle cx="20" cy="20" r="13"/><path d="M7 20h26M20 7c5 4 5 22 0 26M20 7c-5 4-5 22 0 26"/></svg></div><h3>Donation<br>Pages</h3><p>Lorem ipsum dolor sit amet consectetur adipiscing elit dolor</p></div>
  <div class="tile" style="left:471px;top:326px"><div class="gold-circle"><svg width="40" height="40" viewBox="0 0 40 40" fill="none" stroke="#fff" stroke-width="2"><rect x="6" y="8" width="28" height="19" rx="1"/><path d="M20 27v5M13 33h14M15 20l8-7M19 21l5-4"/></svg></div><h3>PPC and<br>Funnels</h3><p>Lorem ipsum dolor sit amet consectetur adipiscing elit dolor</p></div>
  <div class="tile" style="left:666px;top:326px"><div class="gold-circle"><svg width="40" height="40" viewBox="0 0 40 40" fill="none" stroke="#fff" stroke-width="2"><rect x="6" y="8" width="28" height="19" rx="1"/><path d="M20 27v5M13 33h14M15 20l8-7M19 21l5-4"/></svg></div><h3>Video<br>Marketing</h3><p>Lorem ipsum dolor sit amet consectetur adipiscing elit dolor</p></div>
  <div class="tile" style="left:861px;top:326px"><div class="gold-circle"><svg width="40" height="40" viewBox="0 0 40 40" fill="none" stroke="#fff" stroke-width="2"><rect x="6" y="8" width="28" height="19" rx="1"/><path d="M20 27v5M13 33h14M15 20l8-7M19 21l5-4"/></svg></div><h3>Analytics And<br>Optimization</h3><p>Lorem ipsum dolor sit amet consectetur adipiscing elit dolor</p></div>
</section>

<section class="why">
  <div class="side" style="left:132px">
    <div class="ring" style="top:60px"><svg width="106" height="106" viewBox="0 0 106 106"><circle cx="53" cy="53" r="50" fill="none" stroke="#444" stroke-width="3"/><circle cx="53" cy="53" r="50" fill="none" stroke="var(--gold)" stroke-width="3.5" stroke-dasharray="292 22" transform="rotate(-70 53 53)"/></svg><span>93%</span></div>
    <div class="rate" style="top:196px">SUCCESS RATE</div>
    <div class="ring" style="top:310px"><svg width="106" height="106" viewBox="0 0 106 106"><circle cx="53" cy="53" r="50" fill="none" stroke="#444" stroke-width="3"/><circle cx="53" cy="53" r="50" fill="none" stroke="var(--gold)" stroke-width="3.5" stroke-dasharray="292 22" transform="rotate(-70 53 53)"/></svg><span>93%</span></div>
    <div class="rate" style="top:446px">SUCCESS RATE</div>
  </div>
  <div class="side" style="left:912px">
    <div class="ring" style="top:60px"><svg width="106" height="106" viewBox="0 0 106 106"><circle cx="53" cy="53" r="50" fill="none" stroke="#444" stroke-width="3"/><circle cx="53" cy="53" r="50" fill="none" stroke="var(--gold)" stroke-width="3.5" stroke-dasharray="292 22" transform="rotate(-70 53 53)"/></svg><span>93%</span></div>
    <div class="rate" style="top:196px">SUCCESS RATE</div>
    <div class="ring" style="top:310px"><svg width="106" height="106" viewBox="0 0 106 106"><circle cx="53" cy="53" r="50" fill="none" stroke="#444" stroke-width="3"/><circle cx="53" cy="53" r="50" fill="none" stroke="var(--gold)" stroke-width="3.5" stroke-dasharray="292 22" transform="rotate(-70 53 53)"/></svg><span>93%</span></div>
    <div class="rate" style="top:446px">SUCCESS RATE</div>
  </div>
  <div class="abs eyebrow" style="left:0;width:1200px;text-align:center;top:47px">Why Chose Us?</div>
  <h2 class="abs title" style="left:0;width:1200px;text-align:center;top:77px">Why We Are Best?</h2>
  <p class="abs copy" style="left:301px;top:114px;width:598px;text-align:center">Lorem ipsum dolor sit amet, consectetur adipiscing elit, sed do eiusmod tempor incididunt ut labore et dolore magna aliqua. Vulputate dignissim suspendisse in est ante. Faucibus turpis in eu mi bibendum neque. Sodales ut etiam sit amet nisl purus. Velit laoreet id donec ultrices tincidunt.</p>

  <div class="perk fill" style="left:302px;top:222px"><div class="gold-circle"><svg width="38" height="38" viewBox="0 0 38 38" fill="none" stroke="#fff" stroke-width="2"><rect x="6" y="7" width="26" height="18"/><path d="M10 12h18M10 16h12M10 20h8M19 25v5M12 31h14"/></svg></div><h4>Best Designer</h4></div>
  <div class="perk" style="left:501px;top:222px"><div class="gold-circle"><svg width="38" height="38" viewBox="0 0 38 38" fill="none" stroke="#fff" stroke-width="2"><rect x="5" y="7" width="28" height="19"/><path d="M19 26v5M12 32h14M12 13h14M12 18h9"/></svg></div><h4>Best Developer</h4></div>
  <div class="perk fill" style="left:699px;top:222px"><div class="gold-circle"><svg width="38" height="38" viewBox="0 0 38 38" fill="none" stroke="#fff" stroke-width="2"><path d="M7 31V23h5v8M16 31V18h5v13M25 31V12h5v19M6 16l8-6 7 4 10-8"/></svg></div><h4>Best Marketing</h4></div>
  <div class="perk" style="left:302px;top:362px"><div class="gold-circle"><svg width="38" height="38" viewBox="0 0 38 38" fill="none" stroke="#fff" stroke-width="2"><circle cx="19" cy="19" r="12"/><circle cx="14" cy="19" r="3"/><circle cx="24" cy="13" r="3"/><circle cx="24" cy="25" r="3"/><path d="M17 18l4-3M17 20l4 3"/></svg></div><h4>Best In Social Media</h4></div>
  <div class="perk fill" style="left:501px;top:362px"><div class="gold-circle"><svg width="38" height="38" viewBox="0 0 38 38" fill="none" stroke="#fff" stroke-width="2"><path d="M9 5h14l6 6v22H9z"/><path d="M13 29v-5M18 29v-9M23 29v-7"/></svg></div><h4>Best In eCommerce</h4></div>
  <div class="perk" style="left:699px;top:362px"><div class="gold-circle"><svg width="38" height="38" viewBox="0 0 38 38" fill="none" stroke="#fff" stroke-width="2"><path d="M9 20a10 10 0 0 1 20 0M8 19h4v7H8zM26 19h4v7h-4zM28 26c0 4-4 6-9 6"/></svg></div><h4>Best Help &amp; Support</h4></div>
  <div class="btn" style="left:296px;top:498px;width:147px;height:33px">Know More <span>»</span></div>
</section>

<section class="portfolio">
  <div class="abs eyebrow" style="left:139px;width:172px;text-align:center;top:52px">Portfolio</div>
  <h2 class="abs title" style="left:139px;width:172px;text-align:center;top:78px;line-height:23px;font-size:20px">Some Of Our Delights Projects</h2>
  <p class="abs" style="left:139px;top:167px;width:172px;text-align:center;font-size:11.6px;line-height:20px;color:var(--muted)">Lorem ipsum dolor sit amet, consectetur adipiscing elit, sed do eiusmod tempor incididunt ut labore et dolore magna aliqua. Vulputate dignissim suspendisse in est ante. Faucibus turpis in eu mi bibendum neque. Sodales ut etiam sit amet nisl purus. Velit laoreet id donec ultrices tincidunt.</p>

  <div class="abs panel-top"></div>
  <div class="abs panel"></div>
  <div class="abs tab-active"></div>
  <div class="tab" style="left:346px;top:72px">Forgeline Safety<br>Programs</div>
  <div class="tab" style="left:511px;top:72px">Pennyleaf<br>Comics</div>
  <div class="tab" style="left:623px;top:72px">Taro<br>Coaches</div>
  <div class="tab" style="left:734px;top:72px">HLDRN</div>
  <div class="tab" style="left:815px;top:72px">VESTIRA</div>
  <div class="tab" style="left:917px;top:72px">1907<br>Communications</div>

  <div class="abs" style="left:380px;top:195px;font-family:var(--head);font-size:14px;text-decoration:underline">ABOUT THE PROJECT</div>
  <p class="abs copy" style="left:350px;top:228px;width:217px;line-height:20px">Forgeline Safety Programs is a workplace safety consulting and training firm that comes to your business, be it a factory, warehouse, manufacturing plant or office, and reviews your safety and training and first response objectives.</p>
  <div class="btn" style="left:350px;top:405px;width:194px;height:34px">Visit The Live Page <span>»</span></div>

  <div class="thumb" role="img" aria-label="Screenshot of the home page" style="left:616px"></div>
  <div class="thumb" role="img" aria-label="Screenshot of the about us page" style="left:730px"></div>
  <div class="thumb" role="img" aria-label="Screenshot of the programs page" style="left:843px"></div>
  <div class="thumb" role="img" aria-label="Screenshot of the benefits page" style="left:953px"></div>
  <div class="thumb-label" style="left:638px">HOME PAGE</div>
  <div class="thumb-label" style="left:752px">ABOUT US<br>PAGE</div>
  <div class="thumb-label" style="left:865px">PROGRAMS<br>PAGE</div>
  <div class="thumb-label" style="left:975px">BENEFITS<br>PAGE</div>
</section>

<section class="testimony">
  <div class="abs t-card">
    <p class="t-quote">“Nec nam aliquam sem et tortor consequat id porta. Ac turpis egestas sed tempus. Gravida neque convallis a cras semper auctor neque vitae. Elit pellentesque habitant morbi tristique senectus et. Viverra nibh cras pulvinar mattis. At erat pellentesque adipiscing commodo. Quam nulla porttitor massa id. Lectus quam id leo in vitae turpis massa. Fames ac turpis egestas sed. Odio ut enim blandit volutpat maecenas volutpat blandit aliquam. Ut porttitor leo a diam sollicitudin tempor id. Sit amet nisl suscipit adipiscing bibendum est ultricies. Odio ut enim blandit volutpat maecenas. Morbi tincidunt augue interdum velit. Urna nunc id cursus metus aliquam eleifend mi in. Tellus at urna condimentum mattis pellentesque id nibh.”</p>
    <div class="abs avatar" role="img" aria-label="Client portrait" style="left:257px;top:247px;width:40px;height:40px"></div>
    <div class="abs" style="left:307px;top:253px;font-family:var(--head);font-size:11px;line-height:15px;font-weight:500">John Doe<br><span style="font-weight:400;font-size:10px">CEO</span></div>
  </div>
  <div class="abs eyebrow" style="left:764px;width:296px;text-align:center;top:50px">Testimony</div>
  <h2 class="abs title" style="left:756px;width:312px;text-align:center;top:84px;font-size:20px;line-height:22px">Check What Our Clients Say</h2>
  <div class="abs t-photo" role="img" aria-label="Photo of three smiling colleagues looking at a phone together"></div>
</section>

<section class="contact">
  <div class="abs eyebrow" style="left:139px;width:297px;text-align:center;top:48px">Contact Us</div>
  <h2 class="abs title" style="left:139px;width:297px;text-align:center;top:82px;font-size:20px">Get In Tuch</h2>
  <div class="abs call-card">
    <div class="photo" role="img" aria-label="Photo of wooden blocks with phone, mobile, email and envelope symbols"></div>
    <div class="abs gold-circle" style="left:131px;top:150px;width:35px;height:35px"><svg width="16" height="16" viewBox="0 0 24 24"><path d="M6.6 10.8a15 15 0 0 0 6.6 6.6l2.2-2.2a1 1 0 0 1 1-.25 11.4 11.4 0 0 0 3.6.57 1 1 0 0 1 1 1V20a1 1 0 0 1-1 1A17 17 0 0 1 3 4a1 1 0 0 1 1-1h3.5a1 1 0 0 1 1 1c0 1.25.2 2.450.57 3.57a1 1 0 0 1-.25 1z" fill="#fff"/></svg></div>
    <div class="abs" style="left:0;width:297px;text-align:center;top:198px;font-family:var(--head);font-size:14px;font-weight:500">CALL US 555-014-2287</div>
  </div>
  <div class="abs form">
    <h2 class="abs title" style="left:0;width:610px;text-align:center;top:17px;font-size:20px">Message Us</h2>
    <span class="field-label" style="left:8px;top:55px">Name</span>
    <span class="field-label" style="left:210px;top:55px">Email</span>
    <span class="field-label" style="left:409px;top:55px">Subject</span>
    <div class="field" style="left:8px;top:70px;width:192px">Name</div>
    <div class="field" style="left:210px;top:70px;width:190px">Email</div>
    <div class="field" style="left:409px;top:70px;width:193px">Subject</div>
    <span class="field-label" style="left:8px;top:118px">Message</span>
    <div class="field" style="left:8px;top:132px;width:594px;height:73px">Message</div>
    <div class="abs" style="left:204px;top:216px;width:203px;height:35px;background:var(--gold);display:flex;align-items:center;justify-content:center;font-family:var(--head);font-size:11.5px;letter-spacing:.5px">» SEND YOUR MESSAGE</div>
  </div>
</section>

<footer class="site-footer">
  <div class="abs" style="left:139px;width:297px;top:62px;text-align:center;color:var(--gold);font-family:var(--head);font-weight:700;line-height:1">
    <div style="font-size:36px;letter-spacing:2px">CORVANE</div>
    <div style="font-size:15px;letter-spacing:7px;margin-top:3px">STRATEGIES</div>
  </div>
  <p class="abs copy" style="left:139px;top:134px;width:297px;font-size:10.5px;line-height:17.5px">Nec nam aliquam sem et tortor consequat id porta. Ac turpis egestas sed tempus. Gravida neque convallis a cras semper auctor neque vitae. Elit pellentesque habitant morbi tristique senectus et. Viverra nibh cras pulvinar mattis. At erat pellentesque adipiscing commodo. Quam nulla porttitor massa id. Lectus quam id leo in vitae turpis massa.</p>

  <div class="f-head" style="left:514px">GET STARTED</div>
  <div class="f-list" style="left:529px">HOME<br>ABOUT<br>SERVICES<br>WHY CHOSE US?<br>PORTFOLIO<br>TESTIMONY<br>CONTACT US</div>
  <div class="f-head" style="left:701px">SERVICES</div>
  <div class="f-list" style="left:716px">Project<br>Our Team<br>Facts<br>Customers</div>
  <div class="f-head" style="left:889px">GET IN TOUCH</div>

  <div class="abs gold-circle" style="left:897px;top:101px;width:35px;height:35px"><svg width="16" height="16" viewBox="0 0 24 24"><path d="M6.6 10.8a15 15 0 0 0 6.6 6.6l2.2-2.2a1 1 0 0 1 1-.25 11.4 11.4 0 0 0 3.6.57 1 1 0 0 1 1 1V20a1 1 0 0 1-1 1A17 17 0 0 1 3 4a1 1 0 0 1 1-1h3.5a1 1 0 0 1 1 1c0 1.25.2 2.45.57 3.57a1 1 0 0 1-.25 1z" fill="#fff"/></svg></div>
  <div class="abs" style="left:947px;top:105px;font-family:var(--head);font-size:13px;line-height:14px;text-align:center">CALL US<br>555-014-2287</div>
  <div class="abs gold-circle" style="left:897px;top:173px;width:35px;height:35px"><svg width="16" height="16" viewBox="0 0 24 24" fill="none" stroke="#fff" stroke-width="2"><circle cx="6" cy="12" r="2.5"/><circle cx="18" cy="6" r="2.5"/><circle cx="18" cy="18" r="2.5"/><path d="M8.2 11l7.6-4M8.2 13l7.6 4"/></svg></div>
  <div class="abs" style="left:947px;top:177px;font-family:var(--head);font-size:13px;line-height:14px;text-align:center">FOLLOW US ON<br>SOCIAL MEDIAS</div>
  <div class="abs" style="left:897px;top:234px;display:flex;gap:8px">
    <span class="gold-circle" style="width:24px;height:24px"></span>
    <span class="gold-circle" style="width:24px;height:24px"></span>
    <span class="gold-circle" style="width:24px;height:24px"></span>
    <span class="gold-circle" style="width:24px;height:24px"></span>
    <span class="gold-circle" style="width:24px;height:24px"></span>
  </div>

  <div class="bottom">© All rights reserved</div>
</footer>

</body>
</html>
```